Business cards Dör Kornhüüs GmbH & Co.KG

We need a uniform business card design template for our employees.
A template should be created to have the same design for all business cards.

Contact Information for Business Card

Firma und Firmierung, Name, Funktion in Unternehmen, Anschrift, Tel. Handynummer, Emailadresse, Internetseite

Colors

Designer to choose colors to be used in the design.

Requirements
Must have
• Our company logo must be on it

```html
<!DOCTYPE html>
<html lang="de">
<head>
<meta charset="utf-8">
<title>Visitenkarte – Dör Kornhüüs</title>
<link rel="stylesheet" href="https://fonts.googleapis.com/css2?family=Libre+Baskerville&display=swap">
<style>
  :root {
    --page: #ffffff;
    --front-a: #952890;
    --front-b: #781d74;
    --arc-a: #c27db3;
    --arc-b: #8a2384;
    --back: #581751;
    --text-light: #f3dcef;
    --brand: #e8717f;
    --icon: #1c0b1b;
  }
  * { margin: 0; padding: 0; box-sizing: border-box; }
  html, body { width: 1200px; height: 1200px; overflow: hidden; background: var(--page); }
  body { position: relative; font-family: "Libre Baskerville", "Times New Roman", serif; }

  .card {
    position: absolute;
    left: 58px;
    width: 422px;
    height: 253px;
    overflow: hidden;
  }
  .card--front { top: 51px; background: linear-gradient(160deg, var(--front-a) 0%, var(--front-b) 100%); }
  .card--back { top: 343px; background: var(--back); }

  .card__arc { position: absolute; inset: 0; }

  .brand-name {
    position: absolute;
    color: var(--brand);
    font-weight: 400;
    white-space: nowrap;
  }
  .card--front .brand-name { left: 27px; top: 30px; font-size: 20px; }
  .card--back .brand-name {
    left: 0; right: 0; top: 50%;
    transform: translateY(-50%);
    text-align: center;
    font-size: 38px;
  }

  .holder { position: absolute; color: var(--text-light); font-size: 13px; }
  .holder__name {
    left: 22px; top: 142px; width: 129px;
    text-align: center;
    border-bottom: 1px solid var(--text-light);
    padding-bottom: 1px;
  }
  .holder__role { left: 15px; top: 199px; }

  .contact-list { position: absolute; left: 204px; top: 120px; list-style: none; }
  .contact-list__item {
    position: absolute;
    left: 0;
    display: flex;
    align-items: center;
    color: var(--text-light);
    font-size: 13px;
    white-space: nowrap;
  }
  .contact-list__icon { width: 14px; height: 14px; margin-right: 15px; flex: none; }
</style>
</head>
<body>

<section class="card card--front" aria-label="Visitenkarte Vorderseite">
  <svg class="card__arc" width="422" height="253" viewBox="0 0 422 253" aria-hidden="true">
    <defs>
      <linearGradient id="arcFill" x1="0" y1="0" x2="1" y2="1">
        <stop offset="0" stop-color="var(--arc-a)"/>
        <stop offset="0.7" stop-color="var(--arc-b)"/>
      </linearGradient>
    </defs>
    <circle cx="382" cy="200" r="204" fill="url(#arcFill)"/>
  </svg>

  <div class="brand-name">Dör Kornhüüs</div>

  <div class="holder holder__name">Name:</div>
  <div class="holder holder__role">Funktion in Unternehmen</div>

  <ul class="contact-list">
    <li class="contact-list__item" style="top:0">
      <svg class="contact-list__icon" viewBox="0 0 14 14"><path d="M7 1a4 4 0 0 0-4 4c0 3 4 7 4 7s4-4 4-7a4 4 0 0 0-4-4zm0 5.5A1.5 1.5 0 1 1 7 3.5a1.5 1.5 0 0 1 0 3z" fill="var(--icon)"/><rect x="5" y="12.5" width="4" height="1" fill="var(--icon)"/></svg>
      Anschrift:
    </li>
    <li class="contact-list__item" style="top:22px">
      <svg class="contact-list__icon" viewBox="0 0 14 14"><circle cx="7" cy="7" r="6" fill="none" stroke="var(--icon)" stroke-width="1"/><path d="M4.5 4.2l1.3-.6.9 1.6-.8.7c.4.9 1 1.5 1.9 1.9l.7-.8 1.6.9-.6 1.3c-2.6 0-5-2.4-5-5z" fill="var(--icon)"/></svg>
      Tel.
    </li>
    <li class="contact-list__item" style="top:44px">
      <svg class="contact-list__icon" viewBox="0 0 14 14"><rect x="4" y="1" width="6" height="12" rx="1" fill="var(--icon)"/><rect x="5" y="2.5" width="4" height="3.5" fill="var(--text-light)"/></svg>
      Handynummer:
    </li>
    <li class="contact-list__item" style="top:74px">
      <svg class="contact-list__icon" viewBox="0 0 14 14"><circle cx="7" cy="7" r="6.5" fill="var(--icon)"/><rect x="3.5" y="5" width="7" height="4.5" fill="none" stroke="var(--text-light)" stroke-width="0.8"/><path d="M3.5 5l3.5 2.5L10.5 5" fill="none" stroke="var(--text-light)" stroke-width="0.8"/></svg>
      Emailadresse:
    </li>
    <li class="contact-list__item" style="top:104px">
      <svg class="contact-list__icon" viewBox="0 0 14 14" fill="none" stroke="var(--icon)" stroke-width="1"><circle cx="7" cy="7" r="6"/><ellipse cx="7" cy="7" rx="2.6" ry="6"/><path d="M1 7h12M2 4h10M2 10h10"/></svg>
      Internetseite:
    </li>
  </ul>
</section>

<section class="card card--back" aria-label="Visitenkarte Rückseite">
  <div class="brand-name">Dör Kornhüüs</div>
</section>

</body>
</html>
```